Diet product based by mushroom

My company name is HealtHomeIt means heal + home(healing & safe)Our target is women who are twenties - thirties having job & desire to lose weight within short terms about a week, two weeks, a monthMy company makes diet product based on mushrooms So we are looking for this packaging design of black mushroom + enoki mushroom. This product consists of one set(10 stick - each stick 3g) My company's main color is pastel yellow wish & white and company's mission is whoever we make relationship helps their life with mentally, physically We would like to see designs that use the color of our company logoThank you

Target Market(s)

Women who are twenties, thirties having job & desire to lose weight within short terms about a week, two weeks, a month

Colors
f6faec
eaf2ce
cadf82
abd036
9bcb3b

Requirements
Must have
• My project must have logo's color, the word (다온채, the food of gods')
• simple
Nice to have
• simple & highlight,legibility, simple&white
Should not have
• unbalance

```html
<!DOCTYPE html>
<html lang="ko">
<head>
<meta charset="utf-8">
<title>다온채 – Stick Pack Fronts</title>
<link rel="stylesheet" href="https://fonts.googleapis.com/css2?family=Noto+Sans+KR:wght@500;700&family=Questrial&family=Advent+Pro:wght@500&display=swap">
<style>
  :root {
    --page: #ffffff;
    --leaf: #badb94;
    --mist: #f0f7e8;
    --leaf-soft: #cfe5b0;
    --leaf-text: #badb90;
    --ink: #6d6d6d;
    --cut: #7a7a7a;
    --white: #ffffff;
  }
  * { margin: 0; padding: 0; box-sizing: border-box; }
  html, body {
    width: 1200px; height: 934px; overflow: hidden;
    background: var(--page);
  }
  .sheet { position: relative; width: 1200px; height: 934px; }
  .pack {
    position: absolute; top: 77px;
    width: 501px; height: 779px;
    text-align: center;
  }
  .pack--leaf { left: 70px; background: var(--leaf); }
  .pack--mist { left: 626px; background: var(--mist); }

  .pack__flap-name {
    position: absolute; top: 42px; right: 38px;
    font-family: "Noto Sans KR", sans-serif; font-weight: 500;
    font-size: 64px; line-height: 1; letter-spacing: 2px;
  }
  .pack--leaf .pack__flap-name { color: var(--leaf-soft); }
  .pack--mist .pack__flap-name { color: var(--leaf-text); }

  .pack__cutline {
    position: absolute; left: 0; top: 208px;
    width: 501px; height: 90px;
  }

  .pack__brand {
    position: absolute; left: 0; right: 0; top: 448px;
    font-family: "Noto Sans KR", sans-serif; font-weight: 500;
    font-size: 126px; line-height: 1; letter-spacing: 4px;
    color: var(--ink);
  }
  .pack__tagline {
    position: absolute; left: 0; right: 0; top: 678px;
    font-family: "Questrial", sans-serif;
    font-size: 44px; line-height: 1;
  }
  .pack--leaf .pack__tagline { color: var(--white); }
  .pack--mist .pack__tagline { color: var(--leaf-text); }

  .pack__contents {
    position: absolute; left: 0; right: 0; top: 775px;
    font-family: "Advent Pro", sans-serif; font-weight: 500;
    font-size: 25px; line-height: 1; letter-spacing: 1px;
    color: var(--ink);
  }
  .pack__contents { top: 698px; }
  .pack__tagline { top: 606px; }
  .pack__brand { top: 370px; }
</style>
</head>
<body>
<main class="sheet">
  <section class="pack pack--leaf">
    <p class="pack__flap-name">다온채</p>
    <svg class="pack__cutline" viewBox="0 0 501 90" aria-hidden="true">
      <g fill="none" stroke="var(--cut)" stroke-width="1" stroke-dasharray="6 4">
        <line x1="0" y1="1" x2="501" y2="1"/>
        <path d="M167 1 A83 83 0 0 0 333 1"/>
      </g>
      <line x1="333" y1="1" x2="333" y2="12" stroke="var(--cut)" stroke-width="1"/>
    </svg>
    <h1 class="pack__brand">다온채</h1>
    <p class="pack__tagline">the food of gods</p>
    <p class="pack__contents">10 STICKS - EACH STICK 3G</p>
  </section>

  <section class="pack pack--mist">
    <p class="pack__flap-name">다온채</p>
    <svg class="pack__cutline" viewBox="0 0 501 90" aria-hidden="true">
      <g fill="none" stroke="var(--cut)" stroke-width="1" stroke-dasharray="6 4">
        <line x1="0" y1="1" x2="501" y2="1"/>
        <path d="M167 1 A83 83 0 0 0 333 1"/>
      </g>
      <line x1="333" y1="1" x2="333" y2="12" stroke="var(--cut)" stroke-width="1"/>
    </svg>
    <h1 class="pack__brand">다온채</h1>
    <p class="pack__tagline">the food of gods</p>
    <p class="pack__contents">10 STICKS - EACH STICK 3G</p>
  </section>
</main>
</body>
</html>
```